Dental Design, very professional and noticable

Tindale Ridge Dental Surgery is based in Pelican Waters. We are a fast growing dental surgery and are looking for some professional business cards to send to patients.
We would like to see a design that is Vertical and uses the colours Soft Blue, Silver, White and Black. Maybe a full blue side with moto and details on back? Any other ideas or colours that you may think will make the card look unique is fine.
We need all details on the card that are listed above

Target Market(s)

Families, Retired, Other Professionals and Businesses

Industry/Entity Type

Dental

Contact Information for Business Card

Tindale Ridge Dental Surgery
Family, Cosmetic, Preventative
Dr. Owen Castrey
Dental Surgeon
BDS (Adel) FAE FADI FICD FPFA
phone: (07)50001846
fax: (07)50002917
email: tindaleridgedental@quillpost.com
http://tindaleridgedental.com

Logo Text

Logo styles of interest
Abstract Logo
Requirements
Must have
• Vertical, Vibrant but Professional, Rounded Edges, Logo on front and back of card (different colours on each side)
Nice to have
• One side completely blue (not sure what shade) with logo and moto on bottom
Other side white, with blue or different coloured logo with details in black and silver?
Logo should show half circle with 1 end as arrow symbolizing pelican waters canal also a magnifine glass also half circled with 1 end as arrow. Any other ideas are welcome.
Should not have
• A tooth. A smile. Toothbrush or Toothpaste. Cornered edges.

```html
<!DOCTYPE html>
<html lang="en">
<head>
<meta charset="utf-8">
<title>Tindale Ridge Dental Surgery – Business Card</title>
<link rel="stylesheet" href="https://fonts.googleapis.com/css2?family=Roboto+Condensed:wght@400;700&display=swap">
<style>
  :root {
    --frame: #231f20;
    --paper: #ffffff;
    --ink: #231f20;
    --ink-soft: #3d3d3f;
    --soft-blue: #6aabd9;
    --silver: #eeeef0;
    --silver-fade: rgba(238, 238, 240, 0);
  }
  html, body {
    margin: 0;
    padding: 0;
    width: 693px;
    height: 1200px;
    overflow: hidden;
    background: var(--frame);
  }
  .card {
    position: relative;
    width: 693px;
    height: 1200px;
    background: var(--frame);
    font-family: "Roboto Condensed", "Arial Narrow", sans-serif;
  }
  .card__face {
    position: absolute;
    left: 18px;
    top: 18px;
    width: 657px;
    height: 1164px;
    background: var(--paper);
    border-radius: 58px;
    overflow: hidden;
  }
  .backdrop {
    position: absolute;
    left: 60px;
    top: 480px;
    width: 700px;
    height: 760px;
    border-radius: 50%;
    background: radial-gradient(ellipse at 55% 45%, var(--silver) 0%, var(--silver) 45%, var(--silver-fade) 72%);
  }
  .brand-mark {
    position: absolute;
    left: 38px;
    top: 58px;
    display: flex;
    align-items: center;
    gap: 20px;
  }
  .brand-mark__dot {
    width: 150px;
    height: 150px;
    border-radius: 50%;
    background: var(--soft-blue);
  }
  .brand-mark__name {
    font-weight: 700;
    font-size: 36px;
    color: var(--soft-blue);
  }
  .practice {
    position: absolute;
    left: 29px;
    top: 267px;
    margin: 0;
    white-space: nowrap;
  }
  .practice__name {
    display: block;
    font-weight: 700;
    font-size: 50px;
    line-height: 1;
    color: var(--ink);
  }
  .practice__tagline {
    display: block;
    margin-top: 14px;
    font-weight: 700;
    font-size: 43px;
    line-height: 1;
    color: var(--soft-blue);
  }
  .dentist {
    position: absolute;
    left: 87px;
    top: 861px;
    margin: 0;
    line-height: 46px;
    color: var(--ink-soft);
    white-space: nowrap;
  }
  .dentist__name {
    display: block;
    font-weight: 700;
    font-size: 35px;
    color: var(--soft-blue);
  }
  .dentist__credentials {
    display: block;
    font-size: 32px;
  }
  .contact {
    position: absolute;
    left: 87px;
    top: 982px;
    margin: 0;
    padding: 0;
    list-style: none;
    font-size: 32px;
    line-height: 46px;
    color: var(--ink-soft);
    white-space: nowrap;
  }
</style>
</head>
<body>
  <div class="card">
    <div class="card__face">
      <div class="backdrop" role="img" aria-label="Large faint silver background decoration"></div>

      <div class="brand-mark">
        <span class="brand-mark__dot"></span>
        <span class="brand-mark__name">Tindale Ridge</span>
      </div>

      <h1 class="practice">
        <span class="practice__name">Tindale Ridge Dental Surgery</span>
        <span class="practice__tagline">Family, Cosmetic, Preventative</span>
      </h1>

      <p class="dentist">
        <span class="dentist__name">Dr. Owen Castrey Dental Surgeon</span>
        <span class="dentist__credentials">BDS (Adel) FAE FADI FICD FPFA</span>
      </p>

      <ul class="contact">
        <li>phone: (07)50001846</li>
        <li>fax: (07)50002917</li>
        <li>email: tindaleridgedental@quillpost.com</li>
        <li>http://tindaleridgedental.com</li>
      </ul>
    </div>
  </div>
</body>
</html>
```